"VaduMakers" Graphic Design Project

We are a new business creating bath/ body/beauty products. We need label designs for men "Lusto for Men " and women- "Lusto for Women" . Since the collection called Lusto will be used for both- we'd like the labels to look similar but separating the gender look- maybe by a same color variation. Our bottles are amber in color , so we like the beiges, cream, and earthy warm tones - greens- brown-orange- yellow-colors. The labels are for 8 oz amber cosmo round bottles. The height is 7.32inches and the diameter is 1.85 inches.
Our starting line will be Lusto for Men ( Silk Body Wash, Silk Body Lotion and Body Mist) and the same for Lusto for Women.
Updates

Target Market(s)

Our target audience is between 30 to 60 years of age. Salons and private consumers.
I am including attached sample of what was started by me.

Industry/Entity Type

Business

Requirements
Must have
• We would like to incorporate the company name- VaduMakers along with the name of the product- which will be Lusto for Men or Lusto for Women on each label.

On label with company name or somewhere on label we would like a tree to symbolize the beginning, but we are open to suggestions.

```html
<!DOCTYPE html>
<html lang="en">
<head>
<meta charset="utf-8">
<title>Lusto for Men – Silk Body Wash Label</title>
<link href="https://fonts.googleapis.com/css2?family=Quicksand:wght@300;400&display=swap" rel="stylesheet">
<style>
  :root {
    --earth-top: #b4782f;
    --earth-mid: #7a4a26;
    --earth-deep: #4a2f1c;
    --earth-bottom: #241912;
    --cream: #f7eddb;
    --cream-soft: rgba(247, 237, 219, 0.86);
    --cream-muted: rgba(240, 226, 200, 0.76);
    --band-line: rgba(36, 22, 12, 0.6);
    --panel-fill: rgba(247, 232, 205, 0.16);
    --emblem-fill: rgba(247, 237, 219, 0.55);
  }
  html, body {
    margin: 0;
    padding: 0;
    width: 953px;
    height: 1200px;
    overflow: hidden;
    background: #ffffff;
  }
  .label {
    position: relative;
    width: 953px;
    height: 1200px;
    overflow: hidden;
    background: linear-gradient(180deg, var(--earth-top) 0%, var(--earth-mid) 42%, var(--earth-deep) 75%, var(--earth-bottom) 100%);
    font-family: "Quicksand", sans-serif;
    font-weight: 300;
    color: var(--cream);
  }
  .ornament-field {
    position: absolute;
    inset: 0;
    background:
      radial-gradient(ellipse 320px 260px at 560px 200px, rgba(255,240,210,0.10), transparent 70%),
      radial-gradient(ellipse 300px 300px at 160px 760px, rgba(255,240,210,0.07), transparent 70%),
      radial-gradient(ellipse 360px 280px at 820px 900px, rgba(255,240,210,0.08), transparent 70%);
  }
  .spine {
    position: absolute;
    top: 0;
    left: 325px;
    width: 96px;
    height: 1200px;
    background: linear-gradient(90deg, rgba(0,0,0,0.14), rgba(255,240,210,0.05) 50%, rgba(0,0,0,0.16));
  }
  .spine-line {
    position: absolute;
    top: 0;
    width: 1.5px;
    height: 1200px;
    background: var(--band-line);
  }
  .spine-line.first { left: 14px; }
  .spine-line.second { left: 35px; }
  .tree-emblem {
    position: absolute;
    left: 353px;
    top: 248px;
    width: 38px;
    height: 38px;
    border-radius: 50%;
    background: var(--emblem-fill);
  }
  .spine-brand {
    position: absolute;
    left: 372px;
    top: 600px;
    transform: translate(-50%, -50%) rotate(-90deg);
    font-size: 96px;
    font-weight: 300;
    line-height: 1;
    white-space: nowrap;
    color: var(--cream);
  }
  .front {
    position: absolute;
    left: 0;
    top: 0;
    width: 326px;
    height: 1200px;
    text-align: center;
  }
  .product-name {
    position: absolute;
    top: 140px;
    width: 100%;
    font-size: 84px;
    font-weight: 300;
    line-height: 1;
    margin: 0;
  }
  .product-audience {
    position: absolute;
    top: 222px;
    left: 147px;
    font-size: 24px;
    font-weight: 400;
    letter-spacing: 0.5px;
  }
  .product-type {
    position: absolute;
    top: 612px;
    width: 100%;
    font-size: 32px;
    font-weight: 400;
  }
  .product-origin {
    position: absolute;
    top: 1108px;
    width: 100%;
    font-size: 23px;
    font-weight: 400;
    line-height: 1.45;
  }
  .back {
    position: absolute;
    left: 440px;
    top: 0;
    width: 510px;
    height: 1200px;
    text-align: center;
  }
  .description {
    position: absolute;
    top: 93px;
    left: 0;
    width: 510px;
    font-size: 23px;
    line-height: 32px;
  }
  .description p { margin: 0 0 33px; }
  .ingredients-panel {
    position: absolute;
    top: 554px;
    left: 0;
    width: 484px;
    height: 417px;
    border-radius: 14px;
    background: var(--panel-fill);
    box-sizing: border-box;
    padding: 36px 14px 0;
    font-size: 17.5px;
    line-height: 27px;
    color: var(--cream-soft);
    hyphens: manual;
  }
  .contact {
    position: absolute;
    top: 1058px;
    left: 0;
    width: 510px;
    font-size: 23px;
    line-height: 1.42;
    color: var(--cream-muted);
  }
</style>
</head>
<body>
  <main class="label">
    <div class="ornament-field" role="img" aria-label="Faint swirling curl ornament pattern across the label"></div>

    <section class="front">
      <h1 class="product-name">Lusto</h1>
      <div class="product-audience">FOR MEN</div>
      <div class="product-type">Silk Body Wash</div>
      <div class="product-origin">MADE IN USA<br>8.25 fl oz. / 244mL</div>
    </section>

    <div class="spine">
      <span class="spine-line first"></span>
      <span class="spine-line second"></span>
    </div>
    <div class="tree-emblem" role="img" aria-label="Tree emblem symbolising the beginning"></div>
    <div class="spine-brand">VaduMakers</div>

    <section class="back">
      <div class="description">
        <p>Our Nourishing Silk Body Wash will engulf you in luxurious lather as it gently cleanses your delicate skin leaving it soft as silk.</p>
        <p>Directions: Apply to skin while damp with sponge or wash cloth. Rinse well.</p>
        <p>WARNINGS/CAUTIONS: For external use only. Avoid contact with eyes.</p>
        <p>NOT TESTED ON ANIMALS</p>
      </div>

      <div class="ingredients-panel">
        INGREDIENTS: purified water, sodium olefin sulfonate (plant source), organic aloe barbadensis leaf juice, cocamidopropyl betaine (plant source), sodium chloride (salt), kosher vegetable glycerin, tocopherol (natural vitamin E), polysorbate 20 (plant source), potassium sorbate (plant source), phenoxyethanol (mild preservative), caprylyl glycol (plant source), organic anthemis nobilis (chamo&shy;mile) extract, organic calendula officinalis flower extract, xanthan gum (plant source), magnesium ascorbyl phosphate (vitamin C ester), sodium bicarbonate (baking soda), citric acid fragrance.
      </div>

      <div class="contact">
        Vadumakers<br>
        Bath – Body - Home<br>
        Coralton, FL&nbsp; 33990<br>
        Shop 24/7 - www.vadumakers-example.com
      </div>
    </section>
  </main>
</body>
</html>
```